Flyer-Design für Karin Vollrath
Zielgruppe
Ich bin psychologische Beraterin und Heilpraktikerin für Psychotherapie. Ich biete ein Coaching speziell für Mütter (meist Mütter mit neugeborenen Babys) an. Dieses Mütter-Coaching will ich bewerben. Die Flyer werden unter anderen an Ärzte und Hebammen weiter gegeben und dort in den Praxen ausliegen.
Aufgabenstellung
In meinem Logo herrschen die Farben orange und grau vor - es wäre schön, wenn sich diese Farben im Flyer wiederfinden würden - evtl. kombiniert mit mittelblau oder einem hellem grün.
Des weiteren möchte ich später Flyer im Din Lang Format (einseitig) mit anderen Angeboten erstellen. Das sollte mit dem Design dann auch möglich sein.
Der Schrifttyp soll bitte Arial sein, passend zum Logo. Ich habe bei Bildorra Fotos zu dem Thema erstanden, die ich stimmig finde. Diese Bilder sollten im Flyer genutzt werden.
Für diesen Flyer hätte ich gerne das Format: Falzblatt mit Wickelfalz - 279 x 219 mm

```html
<!DOCTYPE html>
<html lang="de">
<head>
<meta charset="utf-8">
<title>Coaching für Mütter – Falzblatt</title>
<link rel="stylesheet" href="https://fonts.googleapis.com/css2?family=Arimo:wght@400;700&display=swap">
<style>
  :root{
    --bg:#dcdcdc;
    --paper:#ffffff;
    --orange:#e39a2d;
    --grey:#6e6e6e;
    --grey-dark:#5a5a5a;
    --band:#e6e4e7;
    --photo-warm:#d9cfc6;
    --photo-cool:#6d7a96;
  }
  *{box-sizing:border-box;margin:0;padding:0}
  html,body{width:1200px;height:1200px;overflow:hidden}
  body{
    background:var(--bg);
    font-family:"Arimo",Arial,sans-serif;
    color:var(--grey);
    display:flex;align-items:center;justify-content:center;gap:40px;
  }
  .spread{display:flex;box-shadow:0 6px 18px rgba(0,0,0,.12)}
  .panel{
    width:275px;height:590px;background:var(--paper);
    display:flex;flex-direction:column;position:relative;
  }
  .spread .panel + .panel{border-left:1px solid #ececec}
  .cover{box-shadow:0 6px 18px rgba(0,0,0,.12)}
  .photo{display:block;width:100%;flex:none}
  .panel-body{padding:14px 18px 0 22px;font-size:10px;line-height:1.42}
  .panel-title{
    text-align:center;font-size:17px;font-weight:700;color:var(--grey-dark);
    letter-spacing:.3px;margin:4px 0 14px;
  }
  .panel-title .accent{color:var(--orange)}
  .situation-list{list-style:none}
  .situation-list li{position:relative;padding-left:20px;margin-bottom:14px;text-align:justify;hyphens:auto}
  .situation-list li::before{
    content:"";position:absolute;left:2px;top:4px;width:7px;height:7px;border-radius:50%;
    background:var(--orange);
  }
  .subhead{text-align:center;font-weight:700;font-size:10px;color:var(--grey-dark);margin:8px 0 2px}
  .copy{text-align:justify;hyphens:auto;margin-bottom:10px}
  .copy .accent{color:var(--orange);font-weight:700}
  .copy em{font-style:italic}
  .cover-slogan{
    text-align:center;font-size:20px;line-height:1.3;color:var(--grey);
    margin-top:34px;
  }
  .brand{margin-top:auto;padding-bottom:38px;text-align:center}
  .brand-name{
    display:inline-flex;align-items:center;gap:6px;
    font-size:19px;font-weight:700;color:var(--orange);letter-spacing:.2px;
  }
  .brand-dot{width:9px;height:9px;border-radius:50%;background:var(--orange)}
  .brand-claim{font-size:13px;font-weight:700;color:var(--grey-dark);margin-top:8px}
  .brand-pillars{font-size:11px;color:var(--grey);margin-top:3px}
</style>
</head>
<body>

<div class="spread">
  <!-- Panel: Ihre Situation -->
  <section class="panel panel-situation">
    <svg class="photo" width="275" height="130" viewBox="0 0 275 130" role="img" aria-label="Fotostreifen: erschöpfte Mutter mit Baby im Arm">
      <defs>
        <linearGradient id="warm" x1="0" y1="0" x2="0" y2="1">
          <stop offset="0" stop-color="#e9e3d8"/><stop offset=".55" stop-color="#b9a79a"/><stop offset="1" stop-color="#6d7a96"/>
        </linearGradient>
      </defs>
      <rect width="275" height="130" fill="var(--band)"/>
      <rect x="0" y="0" width="95" height="130" fill="url(#warm)"/>
      <rect x="135" y="0" width="80" height="130" fill="url(#warm)"/>
      <rect x="245" y="0" width="30" height="130" fill="#eeece8"/>
    </svg>
    <div class="panel-body">
      <h2 class="panel-title"><span class="accent">Ihre</span> Situation</h2>
      <ul class="situation-list">
        <li>Haben Sie sich Ihr Mutterglück anders vorgestellt? – Sie hatten sich so auf Ihr Baby gefreut, aber die Realität ist gar nicht so, wie Sie sie sich das gedacht haben?</li>
        <li>Fühlen Sie sich isoliert: plötzlich sind Sie allein in Ihrem Zuhause mit Ihrem Kind, Ihre Kollegen und Freunde führen weiterhin Ihr früheres Leben – Sie sind aber nicht mehr mit dabei?</li>
        <li>Das Verständnis Ihrer Umgebung für Ihre neue Situation fehlt. Sogar die Partnerschaft ist plötzlich ganz anders als sie es vorher war?</li>
        <li>Der Fokus aller richtet sich fast ausschließlich auf Ihr Kind – doch wo bleiben Sie eigentlich?</li>
        <li>Sie werden nur noch als Mutter wahrgenommen – kaum mehr als die Frau und die Persönlichkeit, die Sie vorher waren und auch immer noch sind?</li>
        <li>Sie fühlen sich oft erschöpft, ratlos, überfordert, unverstanden?</li>
      </ul>
    </div>
  </section>

  <!-- Panel: Meine Unterstützung -->
  <section class="panel panel-support">
    <svg class="photo" width="275" height="110" viewBox="0 0 275 110" role="img" aria-label="Blasses Foto: nachdenkliche Mutter mit Baby">
      <defs>
        <linearGradient id="faint" x1="0" y1="0" x2="0" y2="1">
          <stop offset="0" stop-color="#f1eeea"/><stop offset="1" stop-color="#d8d4d8"/>
        </linearGradient>
      </defs>
      <rect width="275" height="110" fill="url(#faint)"/>
      <rect x="40" y="0" width="30" height="110" fill="var(--band)"/>
      <rect x="150" y="0" width="30" height="110" fill="var(--band)"/>
    </svg>
    <div class="panel-body">
      <h2 class="panel-title"><span class="accent">Meine</span> Unterstützung</h2>
      <h3 class="subhead">Begleitung</h3>
      <p class="copy">Die gute Nachricht: Sie müssen diese belastende Situation nicht allein bewältigen – erleben Sie Erleichterung, indem Sie sich von mir beraten lassen. Genießen SIE im Einzelcoaching, dass nur IHRE Situation zählt und SIE im Mittelpunkt stehen, denn als Coach gehe ich individuell auf Ihre Person und Situation ein.</p>
      <h3 class="subhead">Stärkung</h3>
      <p class="copy">Verlagern Sie mit mir Ihren Fokus auf andere Sichtweisen und neue Wege. Entscheiden Sie sich für einen Weg, der zu Ihnen passt und Sie glücklich macht. Finden Sie die Mutterrolle, die sich für Sie so gut anfühlt, dass Sie Ihr Leben so leben, wie es Ihnen gut tut – im Einklang mit den Bedürfnissen Ihrer Familie.</p>
      <h3 class="subhead">Beratung</h3>
      <p class="copy">Trotz Unmengen an Ratgebern fühlen sich viele Mütter mit ihrer neuen Rolle oft überfordert. Bei mir bleiben Sie nicht allein: gemeinsam finden wir individuelle Antworten auf Ihre persönlichen Fragen. Sie geben das Tempo vor – ich begleite Sie wertschätzend!</p>
    </div>
  </section>

  <!-- Panel: Unser Weg -->
  <section class="panel panel-path">
    <svg class="photo" width="275" height="130" viewBox="0 0 275 130" role="img" aria-label="Foto: Mutter hält schlafendes Baby an der Schulter">
      <defs>
        <linearGradient id="calm" x1="0" y1="0" x2="1" y2="1">
          <stop offset="0" stop-color="#f2f1ea"/><stop offset=".5" stop-color="#c9b9ad"/><stop offset="1" stop-color="#8a8690"/>
        </linearGradient>
      </defs>
      <rect width="275" height="130" fill="var(--band)"/>
      <rect x="60" y="0" width="215" height="130" fill="url(#calm)"/>
    </svg>
    <div class="panel-body">
      <h2 class="panel-title"><span class="accent">Unser</span> Weg</h2>
      <p class="copy">Gemeinsam können wir Ihre Situation durchleuchten: mein Angebot umfasst Einzelcoaching, Gruppencoaching und Telefoncoaching.</p>
      <p class="copy"><span class="accent">Einzelcoaching</span> Sie können wählen: das Coaching kann in meiner Praxis in Lindenfeld oder gern auch bei Ihnen zu Hause stattfinden, so wie es gerade für Sie am besten passt.</p>
      <p class="copy">Die Zeit, die Sie und eventuell auch Ihr Partner sich für ein Coaching nehmen, ist überschaubar: maximal drei bis fünf Sitzungen à 60 Minuten können ausreichen, um Ihre momentane Situation anzuschauen und zu verändern.</p>
      <p class="copy"><span class="accent">Gruppencoaching</span> Ist Einzelcoaching nicht das Richtige für Sie, können Sie sich auch für ein Gruppencoaching entscheiden. Lernen Sie Gleichgesinnte kennen und profitieren Sie in doppelter Hinsicht – nach dem Motto <em>„Lieber gemeinsam als einsam“</em>.</p>
      <p class="copy"><span class="accent">Telefoncoaching</span> Sie bestimmen Ort und Zeit. Dieses Angebot könnte das Richtige für Sie sein, wenn Sie zeitlich oder örtlich gebunden sind.</p>
    </div>
  </section>
</div>

<!-- Cover -->
<section class="panel cover">
  <svg class="photo" width="275" height="280" viewBox="0 0 275 280" role="img" aria-label="Titelfoto: erschöpfte Mutter stützt den Kopf, Baby im Arm">
    <defs>
      <linearGradient id="coverPhoto" x1="0" y1="0" x2="0" y2="1">
        <stop offset="0" stop-color="#eee9df"/><stop offset=".45" stop-color="#c2ada0"/><stop offset=".8" stop-color="#6d7a96"/><stop offset="1" stop-color="#e9e2e2"/>
      </linearGradient>
    </defs>
    <rect width="275" height="280" fill="url(#coverPhoto)"/>
  </svg>
  <p class="cover-slogan">Das Baby ist da<br>und nichts ist mehr<br>wie es war</p>
  <div class="brand">
    <div class="brand-name"><span class="brand-dot"></span>karinvollrath</div>
    <div class="brand-claim">Coaching für Mütter</div>
    <div class="brand-pillars">Begleitung – Stärkung – Beratung</div>
  </div>
</section>

</body>
</html>
```